French flying club (aeroclub) complete wordpress theme

We need a complete wordpress theme to overhaul the look and feel of our aeroclub website.

We are a flying club (aeroclub) based in France, near Paris. We are a non-profit organization providing VFR flight training to members of all ages; our instructors all have extensive experience flying professionally (one of them was captain on the Stratoline!) We have a fleet of 3 aircraft of the same type (Pelvo) that we provide to our members at competitive rates: since we are a non-profit, there are no unnecessary margins on what we charge aside from what’s necessary for renewal of a fun-to-fly fleet!

The club has a very old history (founded in 1950), and was initially founded by female pioneers of aviation in France (corps founded in 1934), serving as flying nurses for the French army in various conflicts and for search-and-rescue missions. Now of course we accept all types of applicants! Our members are genuinely passionate about flying, they care more about time airborne than about the glamour surrounding aviation (not that it does not matter).

We are launching this website design contest because our current website (http://www.aeroclub-kelvo.org/) is somewhat stuck in the ‘90s, and we’d like to give it a new look and feel.

Some designs that caught our attention, to draw inspiration from:
- http://www.volbrumeclub.fr/
- http://www.cieldutal.com/
- http://www.ecole-varnot.com/

Idea would be to provide front page access to the latest pictures and movies taken from our latest flights, a few breaking news, and one click access to a few sections, e.g.:
- our fleet/prices
- instruction options (VFR, night VFR, BIA etc.)
- location and contact info
- history
- a members-private login page for aircraft reservation and planning access, supporting some sort of forum/message board would etc.

When it comes to style, we’re looking for things that relate to our logo colors (blue dominant with some red and white). Our logo can be found at http://www.aeroclub-kelvo.org/images/banners_logos/logo_kelvo.gif (we can provide a higher resolution one upon request).

Attached are a few excerpts from existing pages (zip file). They're in French but content is usually self-explanatory. Explanations can be provided if necessary.

Target Market(s)

We tend to have various ‘segments’ of users:
- Teenagers and young adults looking to learn flying
- Seniors looking to learn flying
- Experienced pilots who are looking for a no-nonsense, flying enthusiast community

Industry/Entity Type

Club

Font styles to use
Sans Serif

Requirements
Must have
• Theme should be supplied as a self-deployable wordpress package that can be deployed on a fresh instance of wordpress (i.e. wordpress-compatible zip archive)

```html
<!DOCTYPE html>
<html lang="en">
<head>
<meta charset="utf-8">
<title>Aeroclub Kelvo</title>
<link href="https://fonts.googleapis.com/css2?family=Open+Sans:wght@400;600;700&family=Oswald:wght@400;500&display=swap" rel="stylesheet">
<style>
:root{
  --blue:#1f74d6;
  --blue-dark:#155bb0;
  --blue-light:#e8f1fb;
  --red:#e23b35;
  --grey-bg:#e9ecef;
  --text:#555b63;
  --footer:#2c2d30;
  --footer-bottom:#1c1d1f;
  --white:#fff;
}
*{box-sizing:border-box;margin:0;padding:0}
html,body{width:857px;height:1200px;overflow:hidden}
body{font-family:"Open Sans",Arial,sans-serif;color:var(--text);background:var(--white);font-size:7px;line-height:1.45}
.container{width:560px;margin:0 auto;position:relative}
/* header */
.site-header{height:88px;position:relative;background:var(--white)}
.brand{position:absolute;left:150px;top:6px;display:flex;align-items:center;gap:8px}
.brand-mark{width:70px;height:70px;border-radius:50%;background:var(--blue)}
.brand-name{font-family:"Oswald",sans-serif;font-size:13px;color:var(--blue);font-weight:500}
.tagline{position:absolute;left:300px;top:8px;width:260px}
.tagline strong{display:block;font-size:10px;color:var(--blue);font-weight:700}
.tagline span{font-size:6.5px;color:#777}
.contact-strip{position:absolute;left:300px;top:44px;display:flex;gap:28px}
.contact-item{display:flex;align-items:center;gap:4px;font-size:6.5px;color:var(--blue);font-weight:600}
.contact-item svg{width:11px;height:11px}
.social{position:absolute;left:572px;top:44px;display:flex;gap:4px}
.social span{width:15px;height:15px;background:var(--blue);display:block}
/* nav */
.main-nav{height:16px;background:#f4f5f7;border-top:1px solid #dde1e6;border-bottom:1px solid #dde1e6}
.main-nav ul{list-style:none;display:flex;width:560px;margin:0 auto}
.main-nav li{font-size:6px;font-weight:700;color:#6a7079;text-transform:uppercase;padding:0 13px;line-height:14px}
.main-nav li.active{background:var(--blue);color:var(--white)}
/* hero */
.hero{height:230px;position:relative;background:linear-gradient(180deg,#9aa6ae 0%,#7c8b93 45%,#5e6a6c 70%,#8d8f86 100%)}
.hero-play{position:absolute;left:50%;top:50%;width:40px;height:40px;margin:-20px 0 0 -20px}
/* content */
.content{background:var(--grey-bg);height:345px;padding-top:6px}
.content .container{display:flex;gap:8px}
.main-col{width:480px}
.side-col{width:72px}
.gallery{background:var(--white);height:80px;border:1px solid #d6dbe0}
.panel-title{height:14px;background:var(--blue);color:var(--white);font-size:6px;font-weight:700;padding-left:6px;line-height:14px;text-transform:uppercase}
.gallery-row{display:flex;align-items:center;gap:6px;padding:9px 8px}
.gallery-arrow{width:8px;height:14px}
.thumb{width:48px;height:40px;background:linear-gradient(180deg,#a9b6c0,#6f7d80)}
.side-btn{display:block;height:20px;background:var(--blue);color:var(--white);font-size:6px;font-weight:700;line-height:20px;padding-left:6px;margin-bottom:3px;text-transform:uppercase;position:relative}
.side-btn::after{content:"";position:absolute;right:5px;top:7px;border-left:4px solid var(--white);border-top:3px solid transparent;border-bottom:3px solid transparent}
.cards{display:flex;gap:10px;margin-top:8px}
.card{width:153px;background:var(--blue);color:var(--white)}
.card-media{height:76px;background:linear-gradient(180deg,#b8c6d2,#7f8e7c)}
.card-body{padding:8px 8px 10px;height:152px;position:relative}
.card-body h3{font-family:"Oswald",sans-serif;font-weight:500;font-size:11px;margin:22px 0 4px;text-transform:uppercase}
.card-body p{font-size:6px;line-height:1.5;opacity:.95}
.more{position:absolute;left:8px;bottom:10px;background:var(--white);color:var(--blue);font-size:5.5px;font-weight:700;padding:2px 8px}
/* history */
.history{background:var(--grey-bg);height:120px}
.history .container{background:var(--white);height:106px;padding:8px 10px}
.history h2{font-size:7px;color:var(--blue);font-weight:700;text-transform:uppercase;margin-bottom:4px}
.history-cols{display:flex;gap:20px;font-size:6px}
.history-cols p{flex:1}
/* map + form */
.locate{display:flex;height:243px}
.map{width:50%;background:linear-gradient(135deg,#e6e4de,#d8dcd3)}
.contact-form{width:50%;background:var(--blue);color:var(--white);padding:16px 20px}
.contact-form h2{font-family:"Oswald",sans-serif;font-weight:400;font-size:14px;margin-bottom:10px;text-transform:uppercase}
.field-row{display:flex;gap:10px}
.field{flex:1;margin-bottom:8px}
.field label{font-size:6px;display:block;margin-bottom:2px}
.field span{display:block;height:12px;background:var(--white)}
.field .area{height:56px}
.send{display:inline-block;background:var(--red);color:var(--white);font-size:6px;font-weight:700;padding:4px 10px}
/* footer */
.site-footer{background:var(--footer);height:114px;color:#b9bdc3}
.footer-cols{display:flex;justify-content:space-between;width:640px;margin:0 auto;padding-top:26px;text-align:center}
.footer-col{width:150px}
.footer-col svg{width:18px;height:18px}
.footer-col h4{font-size:6.5px;color:var(--white);font-weight:700;margin:4px 0 3px;text-transform:uppercase}
.footer-col p{font-size:6px}
.footer-bottom{background:var(--footer-bottom);height:43px;text-align:center;font-size:6px;color:#8f949a;line-height:30px}
</style>
</head>
<body>
<header class="site-header">
  <div class="brand"><span class="brand-mark"></span><span class="brand-name">Aeroclub Kelvo</span></div>
  <div class="tagline">
    <strong>Flying since 1950 · VFR PPL · Pelvo fleet · Paris area</strong>
    <span>Non-profit flying club for pilots of all ages near Paris</span>
  </div>
  <div class="contact-strip">
    <div class="contact-item"><svg viewBox="0 0 24 24"><circle cx="12" cy="12" r="12" fill="#1f74d6"/><path d="M8 6l3 3-2 2c1 2 2 3 4 4l2-2 3 3-2 2c-5 0-10-5-10-10z" fill="#fff"/></svg>01 23 45 67 89<br>Flying line</div>
    <div class="contact-item"><svg viewBox="0 0 24 24"><circle cx="12" cy="12" r="12" fill="#1f74d6"/><path d="M12 5a5 5 0 0 0-5 5c0 4 5 9 5 9s5-5 5-9a5 5 0 0 0-5-5zm0 7a2 2 0 1 1 0-4 2 2 0 0 1 0 4z" fill="#fff"/></svg>12 Rue des Hangars<br>95000 Vaulor</div>
  </div>
  <div class="social"><span></span><span></span><span></span><span></span></div>
</header>

<nav class="main-nav">
  <ul>
    <li class="active">Home</li><li>Aircraft</li><li>Club</li><li>Instruction</li><li>Pricing</li><li>Members</li><li>Gallery</li><li>Contact</li>
  </ul>
</nav>

<section class="hero" role="img" aria-label="Photo of a club aircraft parked in front of the hangar, with a video play button">
  <svg class="hero-play" viewBox="0 0 40 40"><circle cx="20" cy="20" r="19" fill="rgba(255,255,255,.85)"/><path d="M16 12l12 8-12 8z" fill="#1f74d6"/></svg>
</section>

<section class="content">
  <div class="container">
    <div class="main-col">
      <div class="gallery">
        <div class="panel-title">Latest Videos</div>
        <div class="gallery-row">
          <svg class="gallery-arrow" viewBox="0 0 8 14"><path d="M7 1L1 7l6 6" stroke="#1f74d6" stroke-width="2" fill="none"/></svg>
          <div class="thumb" role="img" aria-label="Flight video still"></div>
          <div class="thumb" role="img" aria-label="Flight video still"></div>
          <div class="thumb" role="img" aria-label="Flight video still"></div>
          <div class="thumb" role="img" aria-label="Flight video still"></div>
          <div class="thumb" role="img" aria-label="Flight video still"></div>
          <div class="thumb" role="img" aria-label="Flight video still"></div>
          <div class="thumb" role="img" aria-label="Flight video still"></div>
          <svg class="gallery-arrow" viewBox="0 0 8 14"><path d="M1 1l6 6-6 6" stroke="#1f74d6" stroke-width="2" fill="none"/></svg>
        </div>
      </div>
      <div class="cards">
        <article class="card">
          <div class="card-media" role="img" aria-label="Photo of a club aircraft on the apron"></div>
          <div class="card-body">
            <h3>Latest News</h3>
            <p>The spring flying season is open. New members can book a discovery flight with our instructors and join the weekend club meetings at the hangar.</p>
            <span class="more">Read more</span>
          </div>
        </article>
        <article class="card">
          <div class="card-media" role="img" aria-label="Photo of a club aircraft in flight over fields"></div>
          <div class="card-body">
            <h3>Our Fleet/Prices</h3>
            <p>Three Pelvo aircraft of the same type, kept in top shape and offered to members at fair hourly rates with no margin beyond fleet renewal.</p>
            <span class="more">Read more</span>
          </div>
        </article>
        <article class="card">
          <div class="card-media" role="img" aria-label="Photo of a training aircraft on the grass"></div>
          <div class="card-body">
            <h3>Instruction</h3>
            <p>VFR and night VFR training, BIA courses and refresher flights, taught by instructors with long professional flying careers behind them.</p>
            <span class="more">Read more</span>
          </div>
        </article>
      </div>
    </div>
    <aside class="side-col">
      <span class="side-btn">Charts</span>
      <span class="side-btn">Reservation</span>
      <span class="side-btn">Members</span>
    </aside>
  </div>
</section>

<section class="history">
  <div class="container">
    <h2>History</h2>
    <div class="history-cols">
      <p>Founded in 1950 by female pioneers of French aviation, the club grew from a corps of flying nurses created in 1934 who served the army in several conflicts and flew many search and rescue missions across the country.</p>
      <p>Today the club welcomes every applicant who loves to fly. Our members care about time in the air more than glamour, and they share a friendly, no-nonsense spirit that keeps the club alive after seventy years.</p>
    </div>
  </div>
</section>

<section class="locate">
  <div class="map" role="img" aria-label="Map showing the airfield location"></div>
  <div class="contact-form">
    <h2>Conact Form</h2>
    <div class="field-row">
      <div class="field"><label>Name *</label><span></span></div>
      <div class="field"><label>Email *</label><span></span></div>
    </div>
    <div class="field"><label>Message *</label><span class="area"></span></div>
    <span class="send">Send Message</span>
  </div>
</section>

<footer class="site-footer">
  <div class="footer-cols">
    <div class="footer-col"><svg viewBox="0 0 24 24"><path d="M6 3l4 4-2 3c1 3 3 5 6 6l3-2 4 4-3 3C10 21 3 14 3 6z" fill="#e23b35"/></svg><h4>Phone No.</h4><p>01 23 45 67 89</p></div>
    <div class="footer-col"><svg viewBox="0 0 24 24"><rect x="7" y="2" width="10" height="20" rx="2" fill="#e23b35"/><rect x="9" y="5" width="6" height="12" fill="#2c2d30"/></svg><h4>Mobile No.</h4><p>06 12 34 56 78</p></div>
    <div class="footer-col"><svg viewBox="0 0 24 24"><path d="M12 2a7 7 0 0 0-7 7c0 5 7 13 7 13s7-8 7-13a7 7 0 0 0-7-7zm0 10a3 3 0 1 1 0-6 3 3 0 0 1 0 6z" fill="#e23b35"/></svg><h4>Address</h4><p>12 Rue des Hangars, 95000 Vaulor</p></div>
    <div class="footer-col"><svg viewBox="0 0 24 24"><rect x="2" y="5" width="20" height="14" fill="#e23b35"/><path d="M2 5l10 8 10-8" stroke="#2c2d30" stroke-width="1.5" fill="none"/></svg><h4>Email</h4><p>contact@aeroclub-kelvo.org</p></div>
  </div>
</footer>
<div class="footer-bottom">Copyright © Aeroclub Kelvo 2015 · All rights reserved</div>
</body>
</html>
```